Ordner für Schulungsunterlagen
Zielgruppe
Die stahlwerk Akademie bietet verschiedene Schulungen in den Bereichen Arbeitssicherheit und Brandschutz an.
Aufgabenstellung
Ich möchte gerne für unsere Schulungen Ordner mit einem ansprechenden Design entwerfen lassen. Es sollte sowohl mit Arbeitssicherheit, als auch mit Brandschutz zu tun haben.
Angaben zum Ordner:
- Hebelordner DIN A 4
- Füllhöhe 55mm und 30mm
- mit 2 Ringen
- mit Schlitzösen
- mit Griffloch
- mit Dreiecktasche
- Bedruckung nur auf der Außenseite
- mit Entwurf für Register

```html
<!DOCTYPE html>
<html lang="de">
<head>
<meta charset="utf-8">
<title>stahlwerk Akademie – Ordner Schulungsunterlagen</title>
<link rel="stylesheet" href="https://fonts.googleapis.com/css2?family=Exo+2:wght@400;500;600&family=Kalam:wght@700&display=swap">
<style>
  :root {
    --brand-blue: #2b3487;
    --brand-red: #d42027;
    --paper: #ffffff;
    --backdrop: #ececec;
    --frame: #bdbdbd;
    --photo-light: #e9e2dc;
    --photo-warm: #c9a48f;
    --photo-dark: #6f6a5a;
  }
  html, body {
    margin: 0;
    width: 1200px;
    height: 900px;
    overflow: hidden;
    background: var(--backdrop);
  }
  .binder-cover {
    position: absolute;
    left: 40px;
    top: 179px;
    width: 1120px;
    height: 542px;
    border: 1px solid var(--frame);
    background: var(--paper);
    box-sizing: border-box;
    overflow: hidden;
  }
  .binder-cover svg { display: block; width: 100%; height: 100%; }
  .brand-name { font-family: "Exo 2", sans-serif; font-weight: 600; fill: var(--brand-blue); }
  .contact-text { font-family: "Exo 2", sans-serif; font-weight: 400; fill: var(--paper); font-size: 4.2px; }
  .spine-title { font-family: "Exo 2", sans-serif; font-weight: 400; fill: var(--paper); font-size: 6px; }
  .cover-title { font-family: "Kalam", cursive; font-weight: 700; fill: var(--brand-blue); font-size: 16.5px; }
  .cover-subtitle { font-family: "Exo 2", sans-serif; font-weight: 500; fill: var(--brand-red); font-size: 11.5px; }
  .web-address { font-family: "Exo 2", sans-serif; font-weight: 500; fill: var(--brand-red); font-size: 6.6px; }
  .web-address--small { font-size: 4.2px; }
</style>
</head>
<body>
  <div class="binder-cover">
    <svg viewBox="0 0 795 385" preserveAspectRatio="none" xmlns="http://www.w3.org/2000/svg">
      <defs>
        <linearGradient id="photo-tones" x1="0" y1="0" x2="1" y2="0">
          <stop offset="0" stop-color="var(--photo-light)"/>
          <stop offset="0.45" stop-color="var(--photo-warm)"/>
          <stop offset="1" stop-color="var(--photo-dark)"/>
        </linearGradient>
      </defs>

      <rect class="colour-band" x="0" y="84" width="795" height="270" fill="var(--brand-blue)"/>

      <rect x="441" y="274" width="160" height="80" fill="url(#photo-tones)" role="img" aria-label="Foto: Teilnehmerin in einer Werkstatt vor Brandschutz-Aushängen"/>

      <path class="front-panel" d="M795,134 C770,116 740,110 712,116 C640,132 584,200 584,262 C584,310 604,352 634,385 L795,385 Z" fill="var(--paper)"/>
      <path class="front-arc" d="M795,134 C770,116 740,110 712,116 C640,132 584,200 584,262 C584,310 604,352 634,385" fill="none" stroke="var(--brand-red)" stroke-width="3"/>

      <circle cx="374" cy="42" r="3" fill="var(--brand-red)"/>
      <text class="brand-name" x="379.5" y="43.8" font-size="4.8">stahlwerk Akademie</text>

      <circle cx="673" cy="38" r="5" fill="var(--brand-red)"/>
      <text class="brand-name" x="681" y="41" font-size="8.5">stahlwerk Akademie</text>

      <text class="spine-title" transform="translate(400,212) rotate(-90)">Ihre Schulungsunterlagen</text>

      <g class="contact-block">
        <text class="contact-text" x="30" y="277">stahlwerk – Akademie UG (haftungsbeschränkt)</text>
        <text class="contact-text" x="30" y="288">Nördlicher Wallweg 12</text>
        <text class="contact-text" x="30" y="293.5">99999 Lindenfeld</text>
        <text class="contact-text" x="30" y="302">Fon: +49 000 5550-133</text>
        <text class="contact-text" x="30" y="307.5">Fax: +49 000 5550-144</text>
        <text class="contact-text" x="30" y="316">eMail: kontakt@stahlwerk-akademie.example</text>
        <text class="contact-text" x="30" y="321.5">Web: www.stahlwerk-akademie.example</text>
      </g>
      <line x1="0" y1="331" x2="134" y2="331" stroke="var(--brand-red)" stroke-width="1.6"/>

      <text class="cover-title" x="619" y="230">Brandschutz</text>
      <text class="cover-title" x="619" y="253">Arbeitssicherheit</text>
      <text class="cover-subtitle" x="619" y="293">Ihre Schulungsunterlagen</text>
      <line x1="619" y1="301" x2="795" y2="301" stroke="var(--brand-blue)" stroke-width="1.6"/>

      <text class="web-address web-address--small" x="364" y="372">www.stahlwerk-akademie.example</text>
      <text class="web-address" x="660" y="373">www.stahlwerk-akademie.example</text>
    </svg>
  </div>
</body>
</html>
```